依頼概要
お客様にハガキを出す際に私の顔を使用したスタンプを作りたいと思っています。
似顔絵は、もともと作成済みなので、体の部分は、スーツぽい姿にしてもらえればと思います。
参考にしていただくサイトは、
https://www.sorano-inkan.example/original-stamp/red
上記のサイトでスタンプを作成する予定です。
ハガキを出す際に左側に自分の住所と名前を記入すると思いますが、送る枚数も多い為、その代わりにスタンプを押せたらと思っています。
サイズは、35mm横×70mm高さです。
1、住所
2、会社名
3、代表取締役と名前
この3点と顔のイラストが入った物を組み合わせていただければと思います。
これらの情報は、お願いする人が決定したらお送りします。
納入方法は、
Aiでお願いします。
宜しくお願いいたします。
■ 選んだ理由

シンプルながらお客様に対してありがとうというメッセージも入っていたのが良かったです。

■ 提案者全員のお礼・コメント

素晴らしい提案をいくつもしていただき、なおかつ迅速に対応していただき、ありがとうございました。

```html
<!DOCTYPE html>
<html lang="ja">
<head>
<meta charset="utf-8">
<title>住所スタンプ</title>
<link rel="stylesheet" href="https://fonts.googleapis.com/css2?family=Noto+Sans+JP:wght@500;700;900&display=swap">
<style>
  :root {
    --ink: #0d0d0d;
    --paper: #ffffff;
    --portrait-top: #d9d9d9;
    --portrait-bottom: #9a9a9a;
  }
  html, body {
    margin: 0;
    padding: 0;
    width: 1200px;
    height: 2380px;
    overflow: hidden;
    background: var(--paper);
  }
  .stamp {
    position: relative;
    width: 1200px;
    height: 2380px;
    background: var(--paper);
    color: var(--ink);
    font-family: "Noto Sans JP", sans-serif;
  }
  .portrait {
    position: absolute;
    left: 0;
    top: 0;
    width: 610px;
    height: 930px;
  }
  .company-prefix {
    position: absolute;
    left: 1010px;
    top: 10px;
    width: 190px;
    font-size: 46px;
    font-weight: 700;
    letter-spacing: 0;
    line-height: 1.2;
    white-space: nowrap;
  }
  .company-name {
    position: absolute;
    left: 1020px;
    top: 160px;
    width: 160px;
    display: flex;
    flex-direction: column;
    gap: 28px;
  }
  .company-name span {
    display: block;
    height: 208px;
    background: var(--ink);
  }
  .vertical {
    position: absolute;
    writing-mode: vertical-rl;
    text-orientation: upright;
    white-space: nowrap;
    margin: 0;
  }
  .title {
    left: 760px;
    top: 440px;
    font-size: 72px;
    font-weight: 500;
    line-height: 1;
  }
  .person-name {
    left: 720px;
    top: 890px;
    font-size: 164px;
    font-weight: 900;
    letter-spacing: 160px;
    line-height: 1;
  }
  .address {
    top: 1160px;
    font-weight: 700;
    line-height: 1;
  }
  .address-postal { left: 512px; font-size: 80px; letter-spacing: -4px; }
  .address-city   { left: 384px; font-size: 104px; letter-spacing: 2px; }
  .address-block  { left: 256px; font-size: 96px; }
  .address-building { left: 128px; font-size: 104px; letter-spacing: 2px; }
</style>
</head>
<body>
<main class="stamp">
  <svg class="portrait" viewBox="0 0 610 930" role="img" aria-label="スーツ姿の代表取締役の似顔絵イラスト">
    <defs>
      <linearGradient id="portraitTone" x1="0" y1="0" x2="0" y2="1">
        <stop offset="0" stop-color="var(--portrait-top)"/>
        <stop offset="1" stop-color="var(--portrait-bottom)"/>
      </linearGradient>
    </defs>
    <rect x="0" y="0" width="610" height="930" fill="url(#portraitTone)"/>
  </svg>

  <div class="company-prefix">株式会社</div>
  <div class="company-name" aria-label="会社名">
    <span></span><span></span><span></span><span></span><span></span>
    <span></span><span></span><span></span><span></span>
  </div>

  <p class="vertical title">代表取締役</p>
  <p class="vertical person-name">山田太郎</p>

  <p class="vertical address address-postal">〒〇〇〇-〇〇〇〇</p>
  <p class="vertical address address-city">東京都千代田区丸の内</p>
  <p class="vertical address address-block">〇-〇-〇</p>
  <p class="vertical address address-building">〇〇〇〇〇〇ビル◎階</p>
</main>
</body>
</html>
```